Business Card Design

Business card design.

Business card is to have logo, website address and email address.

Website is www.brightkettle.ie
Email is info@brightkettle.ie
Logo uploaded

I have ordered Business Card Printing via Print Harbor, the Double-sided colour printed option with gloss finish.

Industry/Entity Type

Business

```html
<!DOCTYPE html>
<html lang="en">
<head>
<meta charset="utf-8">
<title>Bright Kettle – Business Card</title>
<link rel="stylesheet" href="https://fonts.googleapis.com/css2?family=Montserrat:wght@400;600;800&display=swap">
<style>
  :root {
    --page-bg: #e4e4e4;
    --brand-red: #ec1c24;
    --brand-red-dark: #d3121a;
    --card-white: #ffffff;
    --ink: #111111;
    --paper-text: #ffffff;
  }
  html, body {
    margin: 0;
    width: 1200px;
    height: 900px;
    overflow: hidden;
    background: var(--page-bg);
    font-family: "Montserrat", sans-serif;
  }
  .sheet {
    position: relative;
    width: 1200px;
    height: 900px;
    display: flex;
    flex-direction: column;
    align-items: center;
    justify-content: center;
    gap: 60px;
  }
  .card {
    width: 560px;
    height: 320px;
    box-sizing: border-box;
    display: flex;
    flex-direction: column;
    align-items: center;
    justify-content: center;
    box-shadow: 0 6px 18px rgba(0,0,0,0.18);
  }
  .card--back {
    background: radial-gradient(ellipse at 55% 35%, var(--brand-red) 0%, var(--brand-red-dark) 100%);
    color: var(--paper-text);
  }
  .card--front {
    background: var(--card-white);
    color: var(--ink);
  }
  .back-mark {
    display: flex;
    align-items: center;
    gap: 12px;
    margin-bottom: 26px;
  }
  .back-mark__dot {
    width: 26px;
    height: 26px;
  }
  .back-mark__name {
    font-weight: 600;
    font-size: 20px;
    letter-spacing: 0.06em;
  }
  .contact__web {
    font-weight: 600;
    font-size: 26px;
    letter-spacing: 0.02em;
    margin: 0 0 8px;
  }
  .contact__mail {
    font-weight: 400;
    font-size: 25px;
    margin: 0;
  }
  .brand {
    display: flex;
    align-items: center;
    gap: 16px;
  }
  .brand__dot {
    width: 40px;
    height: 40px;
  }
  .brand__name {
    font-weight: 800;
    font-size: 44px;
    letter-spacing: 0.01em;
    color: var(--ink);
  }
</style>
</head>
<body>
<main class="sheet">
  <section class="card card--back" aria-label="Business card, reverse side">
    <div class="back-mark">
      <svg class="back-mark__dot" viewBox="0 0 26 26" aria-hidden="true"><circle cx="13" cy="13" r="12" fill="var(--paper-text)"/></svg>
      <span class="back-mark__name">BRIGHTKETTLE</span>
    </div>
    <p class="contact__web">WWW.BRIGHTKETTLE.IE</p>
    <p class="contact__mail">info@brightkettle.ie</p>
  </section>

  <section class="card card--front" aria-label="Business card, front side">
    <div class="brand">
      <svg class="brand__dot" viewBox="0 0 40 40" aria-hidden="true"><circle cx="20" cy="20" r="19" fill="var(--brand-red)"/></svg>
      <span class="brand__name">BRIGHTKETTLE.IE</span>
    </div>
  </section>
</main>
</body>
</html>
```